Health & Nutrition - Business Cards

Needs to look new-age, simple, and elegant. The cards are for my services/counsel in health and nutrition - which include mind, body, and soul. I would like to see something clean and simple but beautiful. Can have a plain background or with a pattern but I don't want it to take away from my contact details. Therefore, my info can be on the back of the card and a nice front design. I really like the flower of life symbol. The name of my business is called Willow Lantern.

Target Market(s)

Clients - men & women age 20-60. Adults, parents, teachers, sick individuals seeking nutrient counseling and dietary management.

Industry/Entity Type

Nutritionist

Contact Information for Business Card

Tomas Brindle
Cell: 345-582-7046
Email: tbrindle@mailvane.net

Colors
33a6d7
33b8a4
add136
ffffff
5c5c5c
f04a50
fbee3f
cedeed
85cae6

Requirements
Nice to have
• Maybe it can have some sort of sacred geometry as well, but not required. Nice to have the colors that I choose in the project but feel free to come up with your own use of colors. Thanks! =)

```html
<!DOCTYPE html>
<html lang="en">
<head>
<meta charset="UTF-8">
<title>Willow Lantern – Business Cards</title>
<link href="https://fonts.googleapis.com/css2?family=Montserrat:wght@600&family=Questrial&display=swap" rel="stylesheet">
<style>
  :root {
    --page-bg: #ffffff;
    --card-bg: #363435;
    --leaf-green: #9ac43b;
    --text-light: #ffffff;
    --text-soft: #e6e6e6;
  }
  * { margin: 0; padding: 0; box-sizing: border-box; }
  html, body {
    width: 1200px; height: 1200px; overflow: hidden;
    background: var(--page-bg);
  }
  .canvas { position: relative; width: 1200px; height: 1200px; }

  .card {
    position: absolute;
    background: var(--card-bg);
    color: var(--text-light);
  }
  .card--front { left: 188px; top: 284px; width: 566px; height: 345px; }
  .card--back  { left: 466px; top: 645px; width: 519px; height: 316px; }

  .brand-dot {
    position: absolute;
    border-radius: 50%;
    background: var(--leaf-green);
  }
  .brand-name {
    position: absolute;
    font-family: "Montserrat", sans-serif;
    font-weight: 600;
    color: var(--text-light);
    white-space: nowrap;
    letter-spacing: 0.2px;
  }
  .person-name {
    position: absolute;
    font-family: "Questrial", sans-serif;
    font-weight: 400;
    color: var(--text-soft);
    white-space: nowrap;
  }

  /* Front */
  .card--front .brand-dot { left: 102px; top: 128px; width: 92px; height: 92px; }
  .card--front .brand-name { left: 214px; top: 139px; font-size: 33px; }
  .card--front .person-name { left: 218px; top: 180px; font-size: 27px; }

  /* Back */
  .card--back .brand-dot { left: 105px; top: 113px; width: 82px; height: 82px; }
  .card--back .brand-name {
    left: 0; width: 294px; top: 205px; text-align: center; font-size: 26px;
  }
  .card--back .divider {
    position: absolute; left: 304px; top: 121px;
    width: 2px; height: 96px; background: var(--text-light);
  }
  .card--back .person-name { left: 338px; top: 130px; font-size: 18px; }
  .contact-line {
    position: absolute; left: 338px;
    display: flex; align-items: center; gap: 8px;
    font-family: "Montserrat", sans-serif; font-weight: 600;
    font-size: 10.5px; color: var(--text-light);
    letter-spacing: 0.3px;
  }
  .contact-line--phone { top: 161px; }
  .contact-line--email { top: 187px; }
  .contact-icon { width: 12px; height: 12px; flex: none; }
</style>
</head>
<body>
<div class="canvas">

  <section class="card card--front" aria-label="Card front">
    <div class="brand-dot"></div>
    <div class="brand-name">Willow Lantern</div>
    <div class="person-name">Tomas Brindle</div>
  </section>

  <section class="card card--back" aria-label="Card back">
    <div class="brand-dot"></div>
    <div class="brand-name">Willow Lantern</div>
    <div class="divider"></div>
    <div class="person-name">Tomas Brindle</div>
    <div class="contact-line contact-line--phone">
      <svg class="contact-icon" viewBox="0 0 24 24" aria-hidden="true">
        <path fill="#ffffff" d="M6.6 2.5l3 4-2 2.2c1 2.8 3 5.4 5.6 7l2.2-1.8 4 3-1.8 3.6C10 19.5 4.5 12.5 3.5 4.5z"/>
      </svg>
      <span>345-582-7046</span>
    </div>
    <div class="contact-line contact-line--email">
      <svg class="contact-icon" viewBox="0 0 24 24" aria-hidden="true">
        <rect x="2" y="5" width="20" height="14" rx="1.5" fill="#ffffff"/>
        <path d="M3.5 7l8.5 6 8.5-6" fill="none" stroke="#363435" stroke-width="2"/>
      </svg>
      <span>tbrindle@mailvane.net</span>
    </div>
  </section>

</div>
</body>
</html>
```